Business cards / Stationery
Stationery
Professional
Tomas Belcourt
DOE, CPT, LMT
1400 North Pelham Road
Austin, Texas 78756
tomas.belcourt@merrowcareclinic.com
www.merrowcareclinic.com

```html
<!DOCTYPE html>
<html lang="en">
<head>
<meta charset="utf-8">
<title>Merrow Care Clinic — Stationery</title>
<link href="https://fonts.googleapis.com/css2?family=Montserrat:wght@700&family=Open+Sans:wght@400;600&display=swap" rel="stylesheet">
<style>
  :root{
    --stage:#e9e6e1;
    --paper:#ffffff;
    --blue:#2a9fd8;
    --grey:#6d6e71;
    --dark:#58595b;
    --line:#c9cacc;
    --faint:#eef0f2;
  }
  *{box-sizing:border-box;margin:0;padding:0}
  html,body{width:1200px;height:514px;overflow:hidden;background:var(--stage);font-family:"Open Sans",Arial,sans-serif;color:var(--grey)}
  .sheet{position:absolute;background:var(--paper);box-shadow:0 2px 6px rgba(0,0,0,.18);overflow:hidden}
  .brand{display:flex;align-items:center;gap:6px;font-family:"Montserrat",Arial,sans-serif;font-weight:700;color:var(--blue);letter-spacing:.02em;line-height:1}
  .brand .dot{border-radius:50%;background:var(--blue);flex:none}
  .emblem{position:absolute;border-radius:50%;background:var(--faint)}
  .footer-text{position:absolute;font-size:4.5px;line-height:1.5;color:var(--grey)}
  .corner-bars{position:absolute;left:0;bottom:12px;display:flex;flex-direction:column;gap:2px}
  .corner-bars span{display:block;height:3px}
  .corner-bars .b1{width:14px;background:var(--dark)}
  .corner-bars .b2{width:10px;background:var(--blue)}

  /* letterhead */
  .letterhead{left:24px;top:29px;width:360px;height:452px}
  .letterhead .brand{position:absolute;left:18px;top:18px;font-size:11px}
  .letterhead .brand .dot{width:14px;height:14px}
  .letterhead .emblem{left:96px;top:150px;width:168px;height:168px}

  /* fax */
  .fax{left:408px;top:29px;width:360px;height:452px}
  .fax h2{position:absolute;left:20px;top:20px;font-family:"Montserrat",Arial,sans-serif;font-size:20px;color:var(--dark)}
  .fax-fields{position:absolute;left:20px;top:62px;width:320px;display:grid;grid-template-columns:1fr 1fr;column-gap:14px;row-gap:10px}
  .fax-field{display:flex;align-items:flex-end;gap:4px;font-size:5px;border-bottom:1px solid var(--line);padding-bottom:1px}
  .fax-rule{position:absolute;left:20px;width:320px;height:2px;background:var(--dark)}
  .fax-checks{position:absolute;left:20px;top:160px;width:320px;display:flex;justify-content:space-between;font-size:5.5px}
  .fax-checks span{display:flex;align-items:center;gap:3px}
  .fax-checks i{width:6px;height:6px;border:1px solid var(--grey);display:inline-block}

  /* business card front */
  .card-front{left:792px;top:29px;width:192px;height:115px}
  .card-front .brand{position:absolute;left:12px;top:14px;font-size:8px}
  .card-front .brand .dot{width:12px;height:12px}
  .card-front .emblem{right:8px;top:6px;width:58px;height:58px}
  .card-band{position:absolute;left:0;top:58px;width:100%;height:9px;background:var(--blue);display:flex;align-items:center;padding-left:12px;gap:6px;color:#fff;font-size:5px;font-weight:600}
  .card-band .role{font-weight:400}
  .card-contact{position:absolute;left:12px;top:74px;font-size:4.5px;line-height:1.55}
  .card-front .corner-bars{bottom:8px;left:auto;right:0;align-items:flex-end}

  /* business card back */
  .card-back{left:996px;top:29px;width:192px;height:115px;background:var(--grey)}
  .card-back .brand{position:absolute;left:0;right:0;top:44px;justify-content:center;font-size:10px;color:#fff}
  .card-back .brand .dot{width:14px;height:14px;background:#fff}
  .card-back .tagline{position:absolute;left:0;right:0;top:60px;text-align:center;font-size:4.5px;color:#dcdde0}
  .card-back .web{position:absolute;right:12px;bottom:10px;font-size:5px;color:#fff}

  /* appointment card */
  .appointment{left:888px;top:216px;width:144px;height:96px}
  .appointment h3{position:absolute;left:10px;top:10px;font-size:6px;font-weight:600;color:var(--dark)}
  .appt-lines{position:absolute;left:10px;top:24px;width:124px;display:grid;grid-template-columns:repeat(4,1fr);gap:6px 6px}
  .appt-lines span{font-size:4.5px;border-bottom:1px solid var(--line);padding-bottom:1px}
  .appointment .appt-band{position:absolute;left:0;bottom:18px;width:100%;height:5px;background:var(--blue)}
  .appointment .appt-note{position:absolute;left:10px;bottom:6px;font-size:4.5px}

  /* envelope */
  .envelope{left:792px;top:360px;width:396px;height:120px}
  .envelope .brand{position:absolute;left:14px;top:14px;font-size:9px}
  .envelope .brand .dot{width:12px;height:12px}
  .envelope .footer-text{left:14px;top:34px}
  .envelope .corner-bars{bottom:10px}
</style>
</head>
<body>

<section class="sheet letterhead" aria-label="Letterhead">
  <div class="brand"><span class="dot"></span>MERROW CARE CLINIC</div>
  <div class="emblem" aria-hidden="true"></div>
  <div class="corner-bars"><span class="b1"></span><span class="b2"></span></div>
  <p class="footer-text" style="left:24px;bottom:12px">1400 North Pelham Road<br>Austin, Texas 78756</p>
  <p class="footer-text" style="left:160px;bottom:12px">P: (512) 555-0148<br>F: (512) 555-0149</p>
  <p class="footer-text" style="left:240px;bottom:12px">tomas.belcourt@merrowcareclinic.com<br>www.merrowcareclinic.com</p>
</section>

<section class="sheet fax" aria-label="Fax cover sheet">
  <h2>FAX</h2>
  <div class="fax-rule" style="top:54px"></div>
  <div class="fax-fields">
    <div class="fax-field">To:</div><div class="fax-field">From:</div>
    <div class="fax-field">Fax:</div><div class="fax-field">Pages:</div>
    <div class="fax-field">Phone:</div><div class="fax-field">Date:</div>
    <div class="fax-field">Re:</div><div class="fax-field">CC:</div>
  </div>
  <div class="fax-rule" style="top:148px"></div>
  <div class="fax-checks">
    <span><i></i>Urgent</span><span><i></i>For Review</span><span><i></i>Please Comment</span><span><i></i>Please Reply</span><span><i></i>Please Recycle</span>
  </div>
  <div class="corner-bars"><span class="b1"></span><span class="b2"></span></div>
  <p class="footer-text" style="left:24px;bottom:12px">1400 North Pelham Road<br>Austin, Texas 78756</p>
  <p class="footer-text" style="left:160px;bottom:12px">P: (512) 555-0148<br>F: (512) 555-0149</p>
  <p class="footer-text" style="left:240px;bottom:12px">tomas.belcourt@merrowcareclinic.com<br>www.merrowcareclinic.com</p>
</section>

<section class="sheet card-front" aria-label="Business card front">
  <div class="emblem" aria-hidden="true"></div>
  <div class="brand"><span class="dot"></span>MERROW CARE CLINIC</div>
  <div class="card-band">Tomas Belcourt <span class="role">DOE, CPT, LMT</span></div>
  <p class="card-contact">1400 North Pelham Road, Austin, Texas 78756<br>P: (512) 555-0148<br>tomas.belcourt@merrowcareclinic.com</p>
  <div class="corner-bars"><span class="b1"></span><span class="b2"></span></div>
</section>

<section class="sheet card-back" aria-label="Business card back">
  <div class="brand"><span class="dot"></span>MERROW CARE CLINIC</div>
  <p class="tagline">Caring for your health</p>
  <p class="web">www.merrowcareclinic.com</p>
</section>

<section class="sheet appointment" aria-label="Appointment card">
  <h3>Next Appointment</h3>
  <div class="appt-lines">
    <span>Mon</span><span>Date</span><span>Time</span><span>am/pm</span>
    <span>Mon</span><span>Date</span><span>Time</span><span>am/pm</span>
  </div>
  <div class="appt-band"></div>
  <p class="appt-note">Please call to reschedule.</p>
</section>

<section class="sheet envelope" aria-label="Envelope">
  <div class="brand"><span class="dot"></span>MERROW CARE CLINIC</div>
  <p class="footer-text">1400 North Pelham Road<br>Austin, Texas 78756</p>
  <div class="corner-bars"><span class="b1"></span><span class="b2"></span></div>
</section>

</body>
</html>
```